Business Card Design Project

We need a business card for our IT services provider business. We provide services to small and medium business, and would like something that reflects the color scheme / branding on our recently updated website - www.tallobrix.com.au

The card type we have chosen is a matte laminated double sided configuration at 86mm x 54mm on 350 GSM cardboard.
Updates

Target Market(s)

Small and Medium Business owners

Industry/Entity Type

Business

Requirements
Must have
• *Details on all cards*

Company Name: Tallobrix Pty Ltd
ABN: 52 683 914 207
Address: 47-49 Pembury Street, Ashcombe Vale, Victoria 3172
Phone: 1300 GRAB UP
Fax: 03 9417 6258
Website: www.tallobrix.com.au
Logo/Handprint Icon

*Person Specific*

```html
<!DOCTYPE html>
<html lang="en">
<head>
<meta charset="utf-8">
<title>Tallobrix Business Card</title>
<link rel="stylesheet" href="https://fonts.googleapis.com/css2?family=Open+Sans:wght@400;600;700&display=swap">
<style>
  :root {
    --bg: #e9e7e3;
    --card-white: #ffffff;
    --navy: #0d3a6e;
    --navy-deep: #08305e;
    --blue-light: #1a5c9c;
    --ink: #1b1b1b;
    --muted: #5a5a5a;
    --label: #a9bdd4;
    --rule: #9a9a9a;
  }
  * { margin: 0; padding: 0; box-sizing: border-box; }
  html, body { width: 1200px; height: 601px; overflow: hidden; }
  body {
    background: var(--bg);
    font-family: "Open Sans", sans-serif;
    position: relative;
  }
  .card {
    position: absolute;
    width: 508px;
    height: 318px;
    box-shadow: 0 2px 6px rgba(0,0,0,0.18);
    overflow: hidden;
  }
  .card-front { left: 55px; top: 89px; background: var(--card-white); }
  .card-back {
    left: 617px; top: 195px;
    background: radial-gradient(ellipse 60% 70% at 40% 45%, var(--blue-light) 0%, var(--navy) 55%, var(--navy-deep) 100%);
  }
  .brand {
    position: absolute; left: 18px; top: 106px;
    display: flex; align-items: center; gap: 8px;
  }
  .brand-mark { width: 12px; height: 12px; border-radius: 50%; background: var(--blue-light); }
  .brand-name { font-size: 28px; font-weight: 600; color: var(--navy); letter-spacing: 0.5px; }
  .divider {
    position: absolute; left: 232px; top: 94px; width: 1px; height: 83px;
    background: var(--rule);
  }
  .person { position: absolute; left: 248px; top: 90px; color: var(--ink); }
  .person-name { font-size: 20px; line-height: 26px; }
  .person-title { font-size: 12px; color: var(--muted); line-height: 16px; }
  .person-contact { margin-top: 14px; font-size: 12.5px; line-height: 21px; }
  .person-contact .key { color: var(--muted); }
  .info-band {
    position: absolute; left: 0; bottom: 0; width: 100%; height: 86px;
    background: linear-gradient(90deg, var(--navy) 0%, var(--blue-light) 55%, var(--navy) 100%);
    color: #fff;
  }
  .info-col { position: absolute; top: 9px; font-size: 12.5px; line-height: 16px; }
  .info-col.company { left: 18px; }
  .info-col.contact { left: 233px; }
  .info-col.legal { left: 361px; }
  .company-name { font-weight: 700; font-size: 14px; line-height: 18px; }
  .label { color: var(--label); }
  .card-back .website {
    position: absolute; left: 71px; top: 156px;
    font-size: 24px; font-weight: 700; color: #e8eef6; letter-spacing: 0.3px;
  }
</style>
</head>
<body>
  <section class="card card-front">
    <div class="brand">
      <span class="brand-mark"></span>
      <span class="brand-name">Tallobrix</span>
    </div>
    <div class="divider"></div>
    <div class="person">
      <p class="person-name">Marcus Hale</p>
      <p class="person-title">Title here?</p>
      <div class="person-contact">
        <p><span class="key">Mobile:</span> 0413 728 590</p>
        <p><span class="key">E-mail:</span> marcus.hale@tallobrix.com.au</p>
      </div>
    </div>
    <div class="info-band">
      <div class="info-col company">
        <p class="company-name">Tallobrix Pty Ltd</p>
        <p class="label">Address:</p>
        <p>47-49 Pembury Street,</p>
        <p>Ashcombe Vale, Victoria 3172</p>
      </div>
      <div class="info-col contact">
        <p class="label" style="margin-top:2px">Phone:</p>
        <p>1300 GRAB UP</p>
        <p class="label" style="margin-top:4px">Fax:</p>
        <p>03 9417 6258</p>
      </div>
      <div class="info-col legal">
        <p class="label" style="margin-top:2px">ABN:</p>
        <p>52 683 914 207</p>
        <p class="label" style="margin-top:4px">Website:</p>
        <p>www.tallobrix.com.au</p>
      </div>
    </div>
  </section>

  <section class="card card-back">
    <p class="website">www.tallobrix.com.au</p>
  </section>
</body>
</html>
```